The Harbourline Aid Trust needs a graphic of their innovation approach

What we need?
- we have designed a new innovation approach (see attached). An innovation approach is the process one goes through in order to design and launch a new product or service.
- This new graphic will be used in meetings to help others understand what innovation is and how we do it. It will also be used in training sessions and be the starting point for innovation training materials we are creating
- We have created this draft graphic by copying and pasting new words over another charities innovation process
- We would like you to use your design magic and create our very own innovation process graphic. We would like it to be neat, simple, non fussy, easy to understand /read and in line with our brand colours
Attached:
1. PowerPoint:
- Slide 1: our innovation process
- Slide 2 explanation of process to bring it to life
- Slide 3&4: brand colours
- Slide 5: inspiration / examples of other processes we like the look of
2. Typeface brand guidelines
We can't wait to see what you come up with! Thank you :)
internal employees
Charity

```html
<!DOCTYPE html>
<html lang="en">
<head>
<meta charset="utf-8">
<title>The Harbourline Aid Trust – Innovation Approach</title>
<link rel="stylesheet" href="https://fonts.googleapis.com/css2?family=Inter:wght@300;400;700;800&display=swap">
<style>
  :root {
    --discover: #f05f5f;
    --discover-soft: #f2b8b8;
    --define: #fbbd4a;
    --define-soft: #fcdfa6;
    --deliver: #5bc5c4;
    --deliver-soft: #a8eaea;
    --ink: #444444;
    --paper: #ffffff;
  }
  html, body {
    margin: 0;
    padding: 0;
    width: 1200px;
    height: 778px;
    overflow: hidden;
    background: var(--paper);
  }
  .process-graphic {
    display: block;
    width: 1200px;
    height: 778px;
    font-family: "Inter", "Helvetica Neue", Arial, sans-serif;
  }
  .path { fill: none; stroke-width: 14; stroke-linecap: butt; }
  .path--dashed { stroke-width: 10; stroke-dasharray: 38 26; }
  .stage-disc { }
  .stage-title { font-weight: 800; font-size: 68px; fill: var(--paper); text-anchor: middle; letter-spacing: -1px; }
  .milestone { font-weight: 300; font-size: 40px; fill: var(--ink); }
  .step-label { font-weight: 800; font-size: 34px; letter-spacing: 1px; }
  .discover { stroke: var(--discover); fill: var(--discover); }
  .define { stroke: var(--define); fill: var(--define); }
  .deliver { stroke: var(--deliver); fill: var(--deliver); }
  .icon { fill: none; stroke: var(--paper); stroke-width: 11; stroke-linecap: round; stroke-linejoin: round; }
  .icon-fill { fill: var(--paper); }
</style>
</head>
<body>
<svg class="process-graphic" viewBox="69 130 2247 1263" preserveAspectRatio="xMidYMid meet" role="img" aria-label="Innovation approach: Discover, Define, Deliver">
  <defs>
    <path id="arc-invalidate" d="M 863 596 A 330 330 0 0 1 1003 297"/>
    <path id="arc-test" d="M 1331 268 A 330 330 0 0 1 1478 402"/>
    <path id="arc-ideate" d="M 1075 1125 A 355 355 0 0 0 1107 944"/>
    <path id="arc-insight" d="M 416 1047 A 345 345 0 0 0 518 1227"/>
    <path id="arc-delivery" d="M 1692 1325 A 355 355 0 0 0 1959 1108"/>
  </defs>

  <!-- Discover stage -->
  <g class="stage stage--discover">
    <path class="path path--dashed" style="stroke: var(--discover-soft)" d="M 462 895 A 300 300 0 0 1 888 708"/>
    <path class="path discover" style="fill:none" d="M 310 718 A 300 300 0 0 1 453 975 A 303 303 0 0 0 860 1257"/>
    <path class="path discover" style="fill:none" d="M 905 1236 A 303 303 0 0 0 1020 840"/>
    <polygon class="discover" points="998,800 1052,834 998,866"/>
    <circle class="discover" cx="291" cy="701" r="21"/>
    <circle class="discover" cx="884" cy="1245" r="21"/>
    <circle class="stage-disc discover" cx="753" cy="975" r="247"/>
    <g class="stage-icon">
      <circle class="icon" cx="735" cy="895" r="38"/>
      <line class="icon" x1="706" y1="924" x2="675" y2="955"/>
      <circle class="icon" cx="775" cy="943" r="44" stroke-width="8"/>
    </g>
    <text class="stage-title" x="753" y="1073">DISCOVER</text>
    <text class="step-label" fill="var(--discover)"><textPath href="#arc-insight">INSIGHT</textPath></text>
    <text class="step-label" fill="var(--discover)"><textPath href="#arc-ideate">IDEATE</textPath></text>
  </g>

  <!-- Define stage -->
  <g class="stage stage--define">
    <path class="path path--dashed" style="stroke: var(--define-soft)" d="M 1060 840 A 303 303 0 0 0 1315 848"/>
    <path class="path define" style="fill:none" d="M 980 790 A 300 300 0 0 1 1165 268"/>
    <path class="path define" style="fill:none" d="M 1220 268 A 300 300 0 0 1 1492 562"/>
    <path class="path define" style="fill:none" d="M 1485 630 A 300 300 0 0 1 1372 808"/>
    <polygon class="define" points="1340,810 1398,832 1352,870"/>
    <circle class="define" cx="1192" cy="267" r="21"/>
    <circle class="define" cx="1490" cy="597" r="21"/>
    <circle class="stage-disc define" cx="1192" cy="567" r="247"/>
    <g class="stage-icon">
      <circle class="icon-fill" cx="1188" cy="525" r="64"/>
      <circle class="define" cx="1188" cy="525" r="52"/>
      <circle class="icon-fill" cx="1188" cy="525" r="40"/>
      <circle class="define" cx="1188" cy="525" r="29"/>
      <circle class="icon-fill" cx="1188" cy="525" r="17"/>
      <line x1="1188" y1="525" x2="1238" y2="475" stroke="var(--define)" stroke-width="18"/>
      <line class="icon" x1="1190" y1="523" x2="1238" y2="475" stroke-width="9"/>
      <polygon class="icon-fill" points="1222,478 1236,460 1238,478 1256,480 1238,496"/>
    </g>
    <text class="stage-title" x="1192" y="672">DEFINE</text>
    <text class="step-label" fill="var(--define)"><textPath href="#arc-invalidate">(IN)VALIDATE</textPath></text>
    <text class="step-label" fill="var(--define)"><textPath href="#arc-test">TEST</textPath></text>
  </g>

  <!-- Deliver stage -->
  <g class="stage stage--deliver">
    <path class="path path--dashed" style="stroke: var(--deliver-soft)" d="M 1465 720 A 304 304 0 0 1 1910 860"/>
    <path class="path deliver" style="fill:none" d="M 1360 850 A 300 300 0 1 0 1924 1032"/>
    <path class="path deliver" style="fill:none" d="M 1928 975 A 300 300 0 0 1 2112 698"/>
    <polygon class="deliver" points="2148,680 2084,680 2112,734"/>
    <circle class="deliver" cx="1925" cy="1003" r="21"/>
    <circle class="stage-disc deliver" cx="1630" cy="975" r="247"/>
    <g class="stage-icon">
      <rect class="icon-fill" x="1548" y="878" width="112" height="88" rx="4"/>
      <path class="icon-fill" d="M 1666 878 H 1710 L 1730 930 V 966 H 1666 Z"/>
      <rect x="1678" y="888" width="30" height="28" fill="var(--deliver)"/>
      <polyline points="1580,912 1602,932 1632,900" fill="none" stroke="var(--deliver)" stroke-width="10" stroke-linecap="round" stroke-linejoin="round"/>
      <line class="icon" x1="1534" y1="900" x2="1556" y2="900" stroke-width="8"/>
      <line class="icon" x1="1534" y1="928" x2="1556" y2="928" stroke-width="8"/>
      <circle class="icon-fill" cx="1588" cy="970" r="20"/>
      <circle cx="1588" cy="970" r="8" fill="var(--deliver)"/>
      <circle class="icon-fill" cx="1690" cy="970" r="20"/>
      <circle cx="1690" cy="970" r="8" fill="var(--deliver)"/>
    </g>
    <text class="stage-title" x="1630" y="1073">DELIVER</text>
    <text class="step-label" fill="var(--deliver)"><textPath href="#arc-delivery">DELIVERY PLAN</textPath></text>
  </g>

  <!-- Milestones -->
  <g class="milestones">
    <text class="milestone" x="285" y="660" text-anchor="middle">Challenge</text>
    <text class="milestone" x="1188" y="223" text-anchor="middle">Concepts</text>
    <text class="milestone" x="1532" y="612">Solution</text>
    <text class="milestone" x="922" y="1281">Opportunity Statement</text>
    <text class="milestone" x="1967" y="1018">Launch</text>
  </g>
</svg>
</body>
</html>
```